QuillMark Business Cards

I need a business card designed for QuillMark. To get an idea of what we do please visit https://formvault.example/para-creadores-3

```html
<!DOCTYPE html>
<html lang="en">
<head>
<meta charset="utf-8">
<title>QuillMark Business Cards</title>
<link href="https://fonts.googleapis.com/css2?family=Montserrat:wght@400;500;700&display=swap" rel="stylesheet">
<style>
:root{
  --bg:#2b2b2b;
  --orange:#e3921e;
  --white:#ffffff;
  --ink:#1e1e1e;
  --grey:#555555;
  --rule:#e8a546;
}
*{margin:0;padding:0;box-sizing:border-box}
html,body{width:1200px;height:1186px;overflow:hidden;background:var(--bg);font-family:"Montserrat",sans-serif}
.sheet{position:relative;width:1200px;height:1186px}
.card{position:absolute;left:150px;width:900px;height:514px;border-radius:34px;overflow:hidden}
.card-front{top:55px;background:var(--orange)}
.card-back{top:617px;background:var(--white)}
.brand{position:absolute;display:flex;align-items:center;gap:34px}
.brand-mark{width:86px;height:86px;border:4px solid currentColor}
.brand-text{position:relative}
.brand-name{font-weight:500;letter-spacing:.32em;line-height:1}
.brand-rule{position:absolute;height:2px}
.brand-tag{font-weight:500;letter-spacing:.42em;font-size:12px;margin-top:10px}
.card-front .brand{left:70px;top:205px;color:var(--white)}
.card-front .brand-mark{width:120px;height:120px}
.card-front .brand-name{font-size:52px}
.card-front .brand-rule{left:300px;top:58px;width:180px;background:var(--white)}
.card-front .brand-tag{font-size:14px}
.card-back .brand{left:70px;top:95px;color:var(--orange)}
.card-back .brand-name{font-size:34px;color:var(--ink)}
.card-back .brand-rule{left:210px;top:40px;width:120px;background:var(--grey)}
.divider{position:absolute;left:420px;right:70px;top:255px;height:1px;background:var(--rule)}
.address{position:absolute;right:70px;top:290px;text-align:right;font-size:17px;font-style:normal;color:var(--ink);line-height:1.35}
.person{position:absolute;left:70px;top:300px}
.person-name{font-weight:700;font-size:28px;color:var(--orange)}
.person-role{font-size:18px;color:var(--ink);margin-top:2px}
.person-rule{width:250px;height:1px;background:var(--rule);margin:14px 0 12px}
.contact{list-style:none;font-size:17px;color:var(--ink)}
.contact li{display:flex;align-items:center;gap:14px;line-height:1.55}
.contact svg{width:14px;height:14px;fill:var(--orange)}
.band{position:absolute;left:0;right:0;bottom:0;height:30px;background:var(--orange)}
.band-end{position:absolute;right:0;bottom:0;width:170px;height:30px;background:var(--grey);border-left:10px solid var(--white)}
</style>
</head>
<body>
<main class="sheet">
  <section class="card card-front">
    <div class="brand">
      <div class="brand-mark"></div>
      <div class="brand-text">
        <div class="brand-name">QUILLMARK</div>
        <div class="brand-rule"></div>
        <div class="brand-tag">DIGITAL NOTARY</div>
      </div>
    </div>
  </section>

  <section class="card card-back">
    <div class="brand">
      <div class="brand-mark"></div>
      <div class="brand-text">
        <div class="brand-name">QUILLMARK</div>
        <div class="brand-rule"></div>
        <div class="brand-tag">DIGITAL NOTARY</div>
      </div>
    </div>
    <div class="divider"></div>
    <address class="address">Pol. Ind. Norte, C/3 nº 12<br>30990 Valdeserra</address>
    <div class="person">
      <div class="person-name">Dana Ortiz</div>
      <div class="person-role">CEO &amp; Founder</div>
      <div class="person-rule"></div>
      <ul class="contact">
        <li><svg viewBox="0 0 16 16"><path d="M3 1h3l1 4-2 1a9 9 0 0 0 5 5l1-2 4 1v3c0 1-1 2-2 2A13 13 0 0 1 1 3c0-1 1-2 2-2z"/></svg>900 12 34 56</li>
        <li><svg viewBox="0 0 16 16"><path d="M1 3h14v10H1zM1 3l7 6 7-6v1.5L8 10 1 4.5z"/></svg>info@formvault.example</li>
        <li><svg viewBox="0 0 16 16"><circle cx="8" cy="8" r="7"/></svg>www.formvault.example</li>
      </ul>
    </div>
    <div class="band"></div>
    <div class="band-end"></div>
  </section>
</main>
</body>
</html>
```